Post card selling a software for elderly visitor security

I need a postcard re-design that will entice children of elderly parents to sign-up to monitor the visitors (via online reporting dashboard) that care for them. These elderly residents live in a nursing home and many can't remember who came in the room to care for them. This is a major safety and security issue and adult children sometimes have no way of knowing who is visiting their parents. Our software provides an online reporting dashboard and sends text messages to adult children when a visitor arrives at the nursing home.

Target Market(s)

women between 50-65

Industry/Entity Type

Nursing Home

Colors

Designer to choose colors to be used in the design.

Requirements
Must have
• Must have Two questions: Are you the Primary Guardian of a resident in this community? If so, would you like to know who is visiting them?
• Must have a desktop computer and phone
• Needs to have a white background

```html
<!DOCTYPE html>
<html lang="en">
<head>
<meta charset="utf-8">
<title>Visitor Alert Postcard</title>
<link href="https://fonts.googleapis.com/css2?family=Roboto:wght@500;700&family=Lato:wght@400;700&family=Montserrat:wght@600;700&display=swap" rel="stylesheet">
<style>
  :root{
    --stage:#525252;
    --navy:#134a7c;
    --navy-deep:#0f4373;
    --green:#3aa53f;
    --lime:#c6dc3c;
    --lime-pale:#dbe99a;
    --olive:#8eab3a;
    --photo-dark:#2e221b;
    --photo-warm:#6b4a36;
    --ink:#1b1b1b;
    --white:#ffffff;
    --stamp:#eeeeee;
  }
  *{box-sizing:border-box;margin:0;padding:0}
  html,body{width:1200px;height:1200px;overflow:hidden;background:var(--stage)}
  .card{position:absolute;background:var(--white);overflow:hidden;box-shadow:0 6px 14px rgba(0,0,0,.35)}
  .card-front{left:266px;top:69px;width:678px;height:526px}
  .card-back{left:264px;top:614px;width:680px;height:528px}
  .card svg.art{position:absolute;left:0;top:0}

  .question{position:absolute;left:18px;font-family:"Roboto",sans-serif;font-weight:700;font-size:29px;line-height:36px;color:var(--navy)}
  .question .accent{color:var(--green)}
  .q-primary{top:29px}
  .q-visiting{top:194px}
  .divider{position:absolute;left:18px;top:181px;width:240px;height:3px;background:var(--ink)}
  .intro{position:absolute;left:18px;top:309px;width:360px;font-family:"Lato",sans-serif;font-size:15.6px;line-height:20.3px;color:var(--ink)}
  .phone{position:absolute;display:flex;align-items:center;font-family:"Montserrat",sans-serif;font-weight:600;color:var(--navy)}
  .front-phone{left:18px;top:426px;font-size:29px;gap:14px}
  .front-url{position:absolute;left:0;bottom:0;width:100%;height:40px;background:var(--navy-deep);color:var(--white);font-family:"Lato",sans-serif;font-size:15px;letter-spacing:1.3px;text-align:center;line-height:40px}

  .badge{position:absolute;left:382px;top:293px;width:168px;height:168px;border-radius:50%;background:var(--lime-pale);display:flex;align-items:center;justify-content:center}
  .badge-inner{width:148px;height:148px;border-radius:50%;background:var(--lime);text-align:center;font-family:"Roboto",sans-serif;padding-top:26px}
  .badge-title{font-weight:700;font-size:23px;color:var(--navy);line-height:26px}
  .badge-trial{font-weight:500;font-size:18px;color:var(--ink);line-height:24px;white-space:nowrap;margin-left:-8px;margin-right:-8px}
  .badge-risk{font-weight:500;font-size:25px;color:var(--ink);line-height:28px}

  .back-intro{position:absolute;left:18px;top:26px;width:320px;font-family:"Lato",sans-serif;font-size:15.6px;line-height:20.3px;color:var(--white)}
  .steps-title{position:absolute;left:26px;top:128px;width:218px;height:33px;border-radius:17px;background:var(--olive);color:var(--white);font-family:"Roboto",sans-serif;font-weight:700;font-size:25px;line-height:33px;text-align:center}
  .steps{position:absolute;left:22px;top:178px;list-style:none;font-family:"Lato",sans-serif;font-size:15.6px;line-height:20.3px;color:var(--white)}
  .steps li{position:absolute;left:0;display:flex;gap:4px;white-space:nowrap}
  .steps li:nth-child(1){top:0}
  .steps li:nth-child(2){top:60px}
  .steps li:nth-child(3){top:144px}
  .stamp{position:absolute;left:615px;top:18px;width:47px;height:46px;background:var(--stamp)}
  .address-line{position:absolute;left:462px;width:200px;height:2px;background:var(--ink)}
  .signup-now{position:absolute;left:45px;top:430px;font-family:"Montserrat",sans-serif;font-weight:700;font-size:22px;letter-spacing:1.5px;color:var(--olive)}
  .back-phone{left:22px;top:462px;font-size:29px;gap:10px}
  .back-url{position:absolute;left:32px;top:498px;display:flex;align-items:center;gap:13px;font-family:"Lato",sans-serif;font-size:15.5px;letter-spacing:1.2px;color:var(--ink)}
</style>
</head>
<body>

<section class="card card-front" aria-label="Postcard front">
  <svg class="art" width="678" height="526" viewBox="0 0 678 526">
    <defs>
      <radialGradient id="photo-tone" cx="0.6" cy="0.45" r="0.7">
        <stop offset="0" stop-color="var(--photo-warm)"/>
        <stop offset="1" stop-color="var(--photo-dark)"/>
      </radialGradient>
    </defs>
    <path d="M398 0 C215 75 230 335 678 482 L678 0 Z" fill="var(--olive)"/>
    <path d="M410 0 C237 80 246 325 678 472 L678 0 Z" fill="var(--navy)"/>
    <path d="M426 0 C262 85 262 308 678 458 L678 0 Z" fill="url(#photo-tone)" role="img" aria-label="Photo of hands holding a smartphone"/>
  </svg>

  <h1 class="question q-primary">Are you the<br>Primary Guardian<br>of a resident in<br>this <span class="accent">community?</span></h1>
  <div class="divider"></div>
  <h2 class="question q-visiting"><span class="accent">If so,</span> would you<br>like to know who<br>is visiting them?</h2>
  <p class="intro">Elderly residents live in a nursing home and many can't remember who came in the room to care for them. This is a major safety and security issue and adult children sometimes have no way of knowing who is visiting their parents.</p>

  <div class="phone front-phone">
    <svg width="44" height="44" viewBox="0 0 44 44" aria-hidden="true">
      <circle cx="22" cy="22" r="20.5" fill="none" stroke="var(--olive)" stroke-width="2"/>
      <path d="M15 12c1-1 2.5-1 3.3.3l2 3.2c.6 1 .3 2-.5 2.7l-1.3 1c.9 2.2 2.6 4 4.8 5l1-1.3c.7-.8 1.8-1 2.7-.4l3.2 2c1.2.8 1.3 2.3.3 3.3l-1.5 1.5c-1.3 1.3-3.4 1.5-5 .6-4.5-2.5-8-6-10.4-10.4-.9-1.6-.7-3.7.6-5z" fill="var(--olive)"/>
    </svg>
    <span>01234567890</span>
  </div>

  <div class="badge">
    <div class="badge-inner">
      <div class="badge-title">SIGN UP</div>
      <div class="badge-trial">30 Day Free Trial</div>
      <div class="badge-risk">No Risk !</div>
    </div>
  </div>

  <div class="front-url">www.companyname.com</div>
</section>

<section class="card card-back" aria-label="Postcard back">
  <svg class="art" width="680" height="528" viewBox="0 0 680 528">
    <path d="M0 0 L345 0 C470 95 445 300 0 440 Z" fill="var(--olive)"/>
    <path d="M0 0 L328 0 C448 90 420 285 0 424 Z" fill="var(--navy)"/>
    <circle cx="396" cy="122" r="72" fill="var(--lime)"/>
    <circle cx="396" cy="122" r="65" fill="var(--photo-warm)" role="img" aria-label="Photo of hands using a laptop and a phone on a desk"/>
  </svg>

  <p class="back-intro">Our software provides an online reporting dashboard and sends text messages to adult children when a visitor arrives at the nursing home.</p>
  <div class="steps-title">Steps to Install</div>
  <ol class="steps">
    <li><span>01</span><span>Lorem ipsum dolor sit amet, consectetur<br>adipiscing elit, sed do eiusmod tempor.</span></li>
    <li><span>02</span><span>Lorem ipsum dolor sit amet,<br>consectetur adipiscing elit, sed<br>do eiusmod tempor.</span></li>
    <li><span>03</span><span>Lorem ipsum dolor<br>&nbsp;sit amet,</span></li>
  </ol>

  <div class="stamp"></div>
  <div class="address-line" style="top:325px"></div>
  <div class="address-line" style="top:353px"></div>
  <div class="address-line" style="top:382px"></div>

  <div class="signup-now">SIGN UP NOW</div>
  <div class="phone back-phone">
    <svg width="30" height="30" viewBox="0 0 44 44" aria-hidden="true">
      <circle cx="22" cy="22" r="20" fill="none" stroke="var(--olive)" stroke-width="2.6"/>
      <path d="M15 12c1-1 2.5-1 3.3.3l2 3.2c.6 1 .3 2-.5 2.7l-1.3 1c.9 2.2 2.6 4 4.8 5l1-1.3c.7-.8 1.8-1 2.7-.4l3.2 2c1.2.8 1.3 2.3.3 3.3l-1.5 1.5c-1.3 1.3-3.4 1.5-5 .6-4.5-2.5-8-6-10.4-10.4-.9-1.6-.7-3.7.6-5z" fill="var(--olive)"/>
    </svg>
    <span>01234567890</span>
  </div>
  <div class="back-url">
    <svg width="18" height="18" viewBox="0 0 18 18" aria-hidden="true" fill="none" stroke="var(--olive)" stroke-width="1.3">
      <circle cx="9" cy="9" r="7.5"/>
      <ellipse cx="9" cy="9" rx="3.2" ry="7.5"/>
      <line x1="1.5" y1="9" x2="16.5" y2="9"/>
      <line x1="2.8" y1="5" x2="15.2" y2="5"/>
      <line x1="2.8" y1="13" x2="15.2" y2="13"/>
    </svg>
    <span>www.companyname.com</span>
  </div>
</section>

</body>
</html>
```